Brantwell Group needs a business card design

We need a new business card design using the logo recently selected in a logo competition on Pixel Forum. Our business is a consultancy specializing in aviation and energy and the winning business card design will promote an image of precision and professionalism with creativity.

Please use the logo with the name on the front of the card and use a complementary font. Make the back white with either the light grey or dark grey logo.

Target Market(s)

Senior finance and legal leaders at aviation and energy companies

Industry/Entity Type

Management Consulting

Contact Information for Business Card

Peter Haldane
President
Brantwell Group

www.brantwellgroup.example

(555) 304-6198
ph@brantwellgroup.example

Requirements
Must have
• Professional font that goes well with the logo font

```html
<!DOCTYPE html>
<html lang="en">
<head>
<meta charset="utf-8">
<title>Brantwell Group – Business Card</title>
<link rel="stylesheet" href="https://fonts.googleapis.com/css2?family=Open+Sans:wght@400;600;700&display=swap">
<style>
  :root {
    --page: #ffffff;
    --card: #ececec;
    --band: #c3c6da;
    --navy: #1f3f73;
    --ink: #1a1a1a;
    --ink-soft: #3a3a3a;
  }
  * { margin: 0; padding: 0; box-sizing: border-box; }
  html, body {
    width: 1200px;
    height: 873px;
    overflow: hidden;
    background: var(--page);
    font-family: "Open Sans", Arial, sans-serif;
  }
  .sheet {
    position: relative;
    width: 1200px;
    height: 873px;
    display: flex;
    align-items: center;
    justify-content: center;
    gap: 60px;
  }
  .card {
    position: relative;
    width: 500px;
    height: 286px;
    background: var(--card);
    overflow: hidden;
    box-shadow: 0 6px 18px rgba(0,0,0,0.18);
  }
  .card-band {
    position: absolute;
    inset: 0;
    width: 100%;
    height: 100%;
  }
  .card-band polygon { fill: var(--band); }

  /* Back: contact details */
  .contact {
    position: absolute;
    top: 30px;
    right: 34px;
    text-align: left;
    font-size: 13px;
    line-height: 1.45;
    color: var(--ink-soft);
  }
  .contact-name { font-weight: 700; color: var(--ink); }
  .contact-label { font-weight: 700; color: var(--ink); margin-right: 4px; }

  /* Front: brand and tagline */
  .brand {
    position: absolute;
    top: 30px;
    left: 32px;
    display: flex;
    align-items: center;
    gap: 8px;
    font-size: 17px;
    font-weight: 600;
    letter-spacing: 0.04em;
    color: var(--navy);
  }
  .brand-square {
    width: 12px;
    height: 12px;
    background: var(--navy);
  }
  .tagline {
    position: absolute;
    top: 32px;
    right: 30px;
    text-align: right;
  }
  .tagline-title {
    font-size: 17px;
    font-weight: 700;
    color: var(--ink);
    letter-spacing: -0.01em;
  }
  .tagline-sectors {
    margin-top: 3px;
    font-size: 10.5px;
    color: var(--ink-soft);
  }
</style>
</head>
<body>
<main class="sheet">

  <section class="card card-back" aria-label="Card back with contact details">
    <svg class="card-band" viewBox="0 0 500 286" aria-hidden="true">
      <polygon points="0,160 500,215 500,286 0,286"/>
    </svg>
    <div class="contact">
      <div class="contact-name">Peter Haldane</div>
      <div>President</div>
      <div>Brantwell Group LLC</div>
      <div><span class="contact-label">T</span>(555) 304-6198</div>
      <div><span class="contact-label">E</span>ph@brantwellgroup.example</div>
    </div>
  </section>

  <section class="card card-front" aria-label="Card front with brand">
    <svg class="card-band" viewBox="0 0 500 286" aria-hidden="true">
      <polygon points="0,150 500,105 500,175 0,230"/>
    </svg>
    <div class="brand">
      <span class="brand-square"></span>
      <span class="brand-name">Brantwell Group</span>
    </div>
    <div class="tagline">
      <div class="tagline-title">Finance and Strategy Consulting</div>
      <div class="tagline-sectors">Aviation · Manufacturing · Energy</div>
    </div>
  </section>

</main>
</body>
</html>
```